business card

Business card for new business.
Red and black corporate colors.
Card can have an Indsutrial feel to it. Feel free to add Rust, Bolted steel, or graphics as you see fit. We provide highly specialized services to the below mentioned industries.
Keep information out of corners so that if I want I can choose rounded corners.
Information
- front. name - title - phone - email
- Rear
Refining - Rail - Infrastructure - Mining - Energy
Calgary - Edmonton - Fort McMurray - Revelstoke - Vancouver

```html
<!DOCTYPE html>
<html lang="en">
<head>
<meta charset="utf-8">
<title>Kestrel business card</title>
<link href="https://fonts.googleapis.com/css2?family=Michroma&family=Russo+One&display=swap" rel="stylesheet">
<style>
  :root {
    --page: #1c1c1e;
    --card-dark: #0f1012;
    --card-mid: #23262b;
    --steel-light: #e2cfcc;
    --steel-mid: #bfa5a2;
    --red: #e3201c;
    --grey: #8e8e8e;
    --white: #f4f4f4;
  }
  * { box-sizing: border-box; margin: 0; padding: 0; }
  html, body { width: 1200px; height: 1200px; overflow: hidden; background: var(--page); }
  .canvas { position: relative; width: 1200px; height: 1200px; }
  .card {
    position: absolute; left: 110px; width: 980px; height: 540px;
    border-radius: 28px; overflow: hidden;
    background: radial-gradient(ellipse at 45% 40%, var(--card-mid) 0%, var(--card-dark) 75%);
    box-shadow: 0 18px 40px rgba(0,0,0,.6);
  }
  .card--rear { top: 50px; }
  .card--front { top: 610px; }
  .steel-strip {
    position: absolute; top: 0; bottom: 0; width: 66px;
    background: linear-gradient(90deg, var(--steel-mid), var(--steel-light) 50%, var(--steel-mid));
  }
  .steel-strip--left { left: 0; }
  .steel-strip--right { right: 0; }
  .brand {
    position: absolute; font-family: "Russo One", sans-serif;
    color: var(--grey); font-size: 96px; letter-spacing: 2px; line-height: 1;
  }
  .card--rear .brand { left: 150px; top: 70px; }
  .card--front .brand { left: 150px; top: 80px; }
  .list { position: absolute; list-style: none; font-family: "Michroma", sans-serif;
    color: var(--white); font-size: 20px; line-height: 38px; letter-spacing: 1px; text-transform: uppercase; }
  .list li { display: flex; align-items: center; gap: 14px; white-space: nowrap; }
  .list svg { width: 14px; height: 16px; flex: none; }
  .services { left: 150px; top: 220px; }
  .cities { left: 590px; top: 300px; }
  .person { position: absolute; left: 150px; top: 345px; font-family: "Russo One", sans-serif; white-space: nowrap; }
  .person__name { color: var(--white); font-size: 46px; line-height: 1; text-transform: uppercase; }
  .person__title { color: var(--red); font-size: 28px; margin-top: 10px; text-transform: uppercase; letter-spacing: 1px; }
  .contact { position: absolute; left: 600px; top: 365px; list-style: none;
    font-family: "Michroma", sans-serif; color: var(--white); font-size: 18px; line-height: 42px; }
  .contact li { display: flex; align-items: center; gap: 14px; white-space: nowrap; }
  .contact svg { width: 20px; height: 20px; flex: none; }
</style>
</head>
<body>
<div class="canvas">

  <section class="card card--rear" aria-label="Card back">
    <div class="steel-strip steel-strip--left" role="img" aria-label="Brushed steel plate with rivets"></div>
    <div class="steel-strip steel-strip--right" role="img" aria-label="Brushed steel plate with rivets"></div>
    <div class="brand">KESTREL</div>
    <ul class="list services">
      <li><svg viewBox="0 0 14 16"><polyline points="3,2 11,8 3,14" fill="none" stroke="#e3201c" stroke-width="4"/></svg>Refining</li>
      <li><svg viewBox="0 0 14 16"><polyline points="3,2 11,8 3,14" fill="none" stroke="#e3201c" stroke-width="4"/></svg>Rail</li>
      <li><svg viewBox="0 0 14 16"><polyline points="3,2 11,8 3,14" fill="none" stroke="#e3201c" stroke-width="4"/></svg>Infrastructure</li>
      <li><svg viewBox="0 0 14 16"><polyline points="3,2 11,8 3,14" fill="none" stroke="#e3201c" stroke-width="4"/></svg>Mining</li>
      <li><svg viewBox="0 0 14 16"><polyline points="3,2 11,8 3,14" fill="none" stroke="#e3201c" stroke-width="4"/></svg>Energy</li>
    </ul>
    <ul class="list cities">
      <li><svg viewBox="0 0 14 16"><polyline points="3,2 11,8 3,14" fill="none" stroke="#e3201c" stroke-width="4"/></svg>Calgary</li>
      <li><svg viewBox="0 0 14 16"><polyline points="3,2 11,8 3,14" fill="none" stroke="#e3201c" stroke-width="4"/></svg>Edmonton</li>
      <li><svg viewBox="0 0 14 16"><polyline points="3,2 11,8 3,14" fill="none" stroke="#e3201c" stroke-width="4"/></svg>Fort McMurray</li>
      <li><svg viewBox="0 0 14 16"><polyline points="3,2 11,8 3,14" fill="none" stroke="#e3201c" stroke-width="4"/></svg>Revelstoke</li>
      <li><svg viewBox="0 0 14 16"><polyline points="3,2 11,8 3,14" fill="none" stroke="#e3201c" stroke-width="4"/></svg>Vancouver</li>
    </ul>
  </section>

  <section class="card card--front" aria-label="Card front">
    <div class="steel-strip steel-strip--left" role="img" aria-label="Brushed steel plate with rivets"></div>
    <div class="steel-strip steel-strip--right" role="img" aria-label="Brushed steel plate with rivets"></div>
    <div class="brand">KESTREL</div>
    <div class="person">
      <div class="person__name">Marcus Holden</div>
      <div class="person__title">Managing Director</div>
    </div>
    <ul class="contact">
      <li><svg viewBox="0 0 24 24"><path d="M6 3l4 4-2 3c1 2 4 5 6 6l3-2 4 4-3 3C10 20 4 14 3 6z" fill="#e3201c"/></svg>555-201-4477</li>
      <li><svg viewBox="0 0 24 24"><rect x="2" y="5" width="20" height="14" fill="#e3201c"/><polyline points="2,5 12,13 22,5" fill="none" stroke="#0f1012" stroke-width="2"/></svg>info@kestrelgroup.com</li>
      <li><svg viewBox="0 0 24 24" fill="none" stroke="#e3201c" stroke-width="2"><circle cx="12" cy="12" r="9"/><ellipse cx="12" cy="12" rx="4" ry="9"/><line x1="3" y1="12" x2="21" y2="12"/></svg>www.kestrelgroup.com</li>
    </ul>
  </section>

</div>
</body>
</html>
```